Email Notification & Marketing Templates

I want to start with something like a newsletter or informational email, but i need Top Tips to Detect Phishing Scams. Something that i can send to users so they can follow it when receiving or exchanging emails. I will also need promotional items for my company that i can send to customers as well. It can be based on on our website QRVLINK.COM

Will also need:
newsletters
announcements
marketing emails
alerts
security notifications

Examples:Items such as Security Awareness Poster Series
Phishing Awareness
Password Security
Email Attachments
QR Code scams
Public WiFi safety

```html
<!DOCTYPE html>
<html lang="en">
<head>
<meta charset="utf-8">
<title>QRV Link Networks – Flyer</title>
<link href="https://fonts.googleapis.com/css2?family=Oswald:wght@400;500;600;700&family=Roboto+Condensed:wght@400;500;700&family=Montserrat:wght@800&family=Yellowtail&display=swap" rel="stylesheet">
<style>
  :root{
    --stage:#2b2b2b;
    --cream:#f6f8dc;
    --cream-top:#f7f8ef;
    --green-deep:#0a5c0a;
    --green:#1f8a14;
    --lime:#6cc40b;
    --lime-soft:#8fd62a;
    --ink:#111;
    --white:#fff;
  }
  *{margin:0;padding:0;box-sizing:border-box}
  html,body{width:964px;height:1200px;overflow:hidden;background:var(--stage)}
  .flyer{
    position:absolute;left:82px;top:0;width:800px;height:1200px;overflow:hidden;
    background:linear-gradient(180deg,var(--cream-top) 0%,var(--cream) 45%,#f3f7d2 100%);
    font-family:"Roboto Condensed",sans-serif;color:var(--ink);
  }
  .shapes,.hero-visual{position:absolute;inset:0}
  .brand{position:absolute;left:40px;top:38px;display:flex;align-items:center;gap:10px}
  .brand-mark{width:18px;height:18px;background:var(--green)}
  .brand-name{font-family:"Oswald",sans-serif;font-weight:700;font-size:44px;color:var(--green);letter-spacing:1px;line-height:1}
  .tagline-script{position:absolute;left:58px;top:204px;font-family:"Yellowtail",cursive;font-size:30px;line-height:1.2;color:var(--white)}
  .headline{position:absolute;left:0;top:0;width:400px;height:600px;font-family:"Oswald",sans-serif;font-weight:700;color:var(--white);text-transform:uppercase;text-shadow:2px 3px 4px rgba(0,0,0,.35)}
  .headline span{position:absolute;left:57px;line-height:1;white-space:nowrap;transform-origin:left top}
  .headline .l1{top:247px;font-size:100px;transform:scaleX(.84)}
  .headline .l2{top:349px;font-size:61px;transform:scaleX(.94)}
  .headline .l3{top:413px;font-size:67px;transform:scaleX(.87)}
  .headline .l4{top:479px;font-size:76px;transform:scaleX(.86)}
  .section-title{position:absolute;font-family:"Oswald",sans-serif;font-weight:700;font-size:53px;line-height:1;white-space:nowrap;
    transform:scaleX(.82);transform-origin:left top;
    background:linear-gradient(180deg,#3aa516,#0d5e08);-webkit-background-clip:text;background-clip:text;color:transparent}
  .what-title{left:387px;top:609px}
  .who-title{left:44px;top:709px}
  .who-sub{position:absolute;left:44px;top:776px;font-family:"Oswald",sans-serif;font-weight:500;font-size:21.5px;color:var(--ink)}
  .who-kicker{position:absolute;left:44px;top:810px;font-family:"Oswald",sans-serif;font-weight:500;font-size:21px;color:var(--green)}
  .who-body{position:absolute;left:44px;top:852px;width:308px;font-size:13px;line-height:19.5px;text-align:justify;color:#222}
  .service{position:absolute;left:388px;width:400px;height:110px}
  .service-title{position:absolute;left:111px;top:-2px;font-family:"Oswald",sans-serif;font-weight:500;font-size:24px;white-space:nowrap;color:var(--ink)}
  .service-text{position:absolute;left:112px;top:38px;width:258px;font-size:10.5px;line-height:13.5px;font-weight:500;text-align:justify;color:#111}
  .s1{top:673px}.s2{top:787px}.s3{top:900px}
  .s3 .service-text{width:194px}
  .phone{position:absolute;left:85px;top:1040px;font-family:"Montserrat",sans-serif;font-weight:800;font-size:43px;line-height:1.2;white-space:nowrap;color:var(--white);text-shadow:1px 2px 3px rgba(0,0,0,.3)}
  .contact{position:absolute;color:var(--white);font-family:"Oswald",sans-serif;font-weight:400;font-size:18.5px;line-height:22px;white-space:nowrap}
  .contact-address{left:76px;top:1131px}
  .contact-email{left:371px;top:1142px}
</style>
</head>
<body>
<main class="flyer">
  <svg class="shapes" width="800" height="1200" viewBox="0 0 800 1200">
    <defs>
      <linearGradient id="heroGreen" x1="0" y1="0" x2="0.3" y2="1">
        <stop offset="0" stop-color="#2f8f1b"/><stop offset="0.6" stop-color="#1a7510"/><stop offset="1" stop-color="#0b5a08"/>
      </linearGradient>
      <linearGradient id="phoneBand" x1="0" y1="0" x2="0" y2="1">
        <stop offset="0" stop-color="#72c70c"/><stop offset="1" stop-color="#2f9410"/>
      </linearGradient>
      <linearGradient id="badge" x1="0" y1="0" x2="0" y2="1">
        <stop offset="0" stop-color="#45b016"/><stop offset="1" stop-color="#0e6609"/>
      </linearGradient>
    </defs>
    <path d="M0,0 H609 V250 L510,530 L340,640 Q270,680 195,668 Q110,652 0,575 Z" fill="var(--lime)"/>
    <path d="M0,0 H609 V240 L500,520 L330,628 Q265,662 195,652 Q110,638 0,560 Z" fill="url(#heroGreen)"/>
    <path d="M0,0 H347 V70 Q347,100 310,115 L200,162 Q150,185 95,170 L0,137 Z" fill="var(--white)"/>
    <path d="M0,1020 H410 Q470,1020 492,1090 V1111 H0 Z" fill="url(#phoneBand)"/>
    <path d="M0,1111 H540 Q600,1115 625,1200 H0 Z" fill="var(--green-deep)"/>
    <g transform="translate(388,673)">
      <path d="M52,0 L104,52 L52,104 L0,52 Z" fill="url(#badge)"/>
      <rect x="43" y="50" width="18" height="14" rx="2" fill="none" stroke="#fff" stroke-width="2"/>
      <path d="M47,50 V45 a5,5 0 0 1 10,0 V50" fill="none" stroke="#fff" stroke-width="2"/>
      <circle cx="52" cy="52" r="20" fill="none" stroke="#fff" stroke-width="1.5" stroke-dasharray="4 3"/>
    </g>
    <g transform="translate(388,787)">
      <path d="M52,0 L104,52 L52,104 L0,52 Z" fill="url(#badge)"/>
      <circle cx="44" cy="44" r="6" fill="none" stroke="#fff" stroke-width="2"/>
      <path d="M33,64 q11,-14 22,0" fill="none" stroke="#fff" stroke-width="2"/>
      <circle cx="63" cy="42" r="6" fill="#fff"/>
      <path d="M50,66 H74 L70,58 H54 Z" fill="none" stroke="#fff" stroke-width="2"/>
    </g>
    <g transform="translate(388,900)">
      <path d="M52,0 L104,52 L52,104 L0,52 Z" fill="url(#badge)"/>
      <circle cx="60" cy="42" r="8" fill="none" stroke="#fff" stroke-width="2.5" stroke-dasharray="3 2"/>
      <path d="M56,42 l3,3 5,-6" fill="none" stroke="#fff" stroke-width="2"/>
      <path d="M32,62 q10,-6 18,0 h10 q6,0 14,-8" fill="none" stroke="#fff" stroke-width="2.5" stroke-linecap="round"/>
      <path d="M40,36 l1,3 3,0 -2,2 1,3 -3,-2 -3,2 1,-3 -2,-2 3,0 Z" fill="#fff"/>
    </g>
    <g transform="translate(46,1057)" fill="none" stroke="#fff" stroke-width="3" stroke-linecap="round">
      <path d="M6,4 q-6,6 2,16 q8,8 14,2 l-4,-5 -4,2 q-4,-3 -6,-6 l2,-4 Z" fill="#fff" stroke="none"/>
      <path d="M14,4 a8,8 0 0 1 8,8"/>
    </g>
    <path d="M55,1130 a8,8 0 0 1 8,8 q0,6 -8,14 q-8,-8 -8,-14 a8,8 0 0 1 8,-8 Z M55,1135 a3,3 0 1 0 0.01,0 Z" fill="var(--lime-soft)" fill-rule="evenodd"/>
    <g transform="translate(344,1149)">
      <rect x="0" y="0" width="17" height="12" fill="var(--lime-soft)"/>
      <path d="M0,0 L8.5,7 L17,0" fill="none" stroke="var(--green-deep)" stroke-width="1.5"/>
    </g>
  </svg>

  <svg class="hero-visual" width="800" height="1200" viewBox="0 0 800 1200">
    <defs>
      <radialGradient id="secure" cx="0.45" cy="0.45" r="0.6">
        <stop offset="0" stop-color="#6fe36a"/><stop offset="0.35" stop-color="#1f7a3a"/><stop offset="1" stop-color="#0f2a2a"/>
      </radialGradient>
    </defs>
    <polygon points="611,170 778,266 778,456 611,552 444,456 444,266" fill="#eef3df" stroke="#eef3df" stroke-width="50" stroke-linejoin="round"/>
    <polygon points="611,170 778,266 778,456 611,552 444,456 444,266" fill="var(--lime)" stroke="var(--lime)" stroke-width="32" stroke-linejoin="round"/>
    <polygon role="img" aria-label="Glowing green security shield with a padlock on a circuit board" points="611,180 769,271 769,451 611,542 453,451 453,271" fill="url(#secure)" stroke="url(#secure)" stroke-width="18" stroke-linejoin="round"/>
  </svg>

  <div class="brand">
    <span class="brand-mark"></span>
    <span class="brand-name">QRV LINK</span>
  </div>

  <div class="tagline-script">QRV Link Networks</div>

  <h1 class="headline">
    <span class="l1">Expert IT</span>
    <span class="l2">Management,</span>
    <span class="l3">Just Around</span>
    <span class="l4">The Corner</span>
  </h1>

  <h2 class="section-title what-title">WHAT WE DO</h2>

  <article class="service s1">
    <h3 class="service-title">Cybersecurity</h3>
    <p class="service-text">Protecting your business is our top priority. We offer robust cybersecurity solutions designed to safeguard your data and infrastructure from threats, ensuring peace of mind.</p>
  </article>
  <article class="service s2">
    <h3 class="service-title">IT Consulting</h3>
    <p class="service-text">With our expert guidance, navigate the ever-evolving landscape of technology to make informed decisions that propel your business forward.</p>
  </article>
  <article class="service s3">
    <h3 class="service-title">Managed Services</h3>
    <p class="service-text">Our proactive IT management keeps your systems running smoothly, so you can focus on what you do best.</p>
  </article>

  <h2 class="section-title who-title">WHO WE ARE</h2>
  <p class="who-sub">Personal Touch, Professional Service</p>
  <p class="who-kicker">YOUR LOCAL IT PARTNERS</p>
  <p class="who-body">At QRV Link Networks, we’re passionate about infusing a personal touch into IT services. Serving the Riverside area, our mission is to provide prompt, reliable, and affordable IT management and support to businesses of all sizes. Founded by Alan Porter and Owen Tesch, our company is rooted in the desire to help businesses thrive through effective IT solutions.</p>

  <div class="phone">(555) 014-2280</div>

  <div class="contact contact-address">48 Mill Brook Ln.<br>Unit 3 &amp; 4, Fairview, KY 40000</div>
  <div class="contact contact-email">info@qrvlink.com</div>
</main>
</body>
</html>
```